Business Card Design

Take existing logo/brand and develop business card for sales team.
We have two separate brands and require a business card for each.

1. VoxHarbor
2. MyNimbusLinko

Refer to our websites www.voxharbor.com.au and www.mynimbuslinko.com.au for designs currently implemented and in the marketplace.

Both cards are brands of our parent company Quorvane Systems Pty Ltd - an Australian Telecommunications company in the medium business sector. We have only business customers, no retail/residential consumers.

Target Market(s)

Australian Business - small to medium enterprise

Industry/Entity Type

Business

Contact Information for Business Card

Ted Ramsell
Sales Director
Mobile: +61 428 163 907
Direct: +61 3 9172 5836
Email: ted@voxharbor.com.au
VoxHarbor (a brand of Quorvane Systems Pty Ltd)

Ted Ramsell
Sales Director
Mobile: +61 428 163 907
Direct: +61 3 9172 5836
Email: ted@mynimbuslinko.com.au
MyNimbusLinko (a brand of Quorvane Systems Pty Ltd)

Font styles to use
Sans Serif
Other font styles liked:
• Roboto Condensed, Open Sans

Requirements
Must have
• Clean lines, crisp fonts - suggest Roboto Condensed or similar.
• Must be easy to read and clear.
• Brand colour #0C8CCD
• Two colour maximum
Nice to have
• Modern, intellectual and unique design.
Should not have
• No die cuts
• No copies or rip-offs of other designs

```html
<!DOCTYPE html>
<html lang="en">
<head>
<meta charset="utf-8">
<title>VoxHarbor and MyNimbusLinko business cards</title>
<link rel="stylesheet" href="https://fonts.googleapis.com/css2?family=Roboto:wght@300;400&family=Roboto+Condensed:wght@400;700&display=swap">
<style>
  :root {
    --brand-blue: #0c8ccd;
    --ink: #1a1a1a;
    --logo-grey: #4a4746;
    --card-dark: #3d3936;
    --paper: #ffffff;
    --label-navy: #1b2150;
  }
  * { margin: 0; padding: 0; box-sizing: border-box; }
  html, body { width: 1200px; height: 1000px; overflow: hidden; background: var(--paper); }
  .sheet { position: relative; width: 1200px; height: 1000px; }

  .card { position: absolute; width: 452px; height: 292px; }
  .card--front { background: var(--paper); box-shadow: 0 2px 10px rgba(0,0,0,0.28); }
  .card--back { background: var(--card-dark); }

  .brand-lockup {
    position: absolute; display: flex; align-items: center; gap: 8px;
    font-family: "Roboto", sans-serif; font-weight: 300; white-space: nowrap;
  }
  .brand-lockup .mark-circle { border-radius: 50%; background: var(--brand-blue); flex: none; }
  .brand-lockup .mark-square { background: var(--brand-blue); flex: none; }
  .front-lockup { left: 40px; top: 34px; font-size: 28px; color: var(--logo-grey); }
  .front-lockup .mark-circle { width: 46px; height: 42px; }
  .front-lockup .mark-square { width: 40px; height: 40px; }

  .contact { position: absolute; left: 135px; top: 124px; }
  .contact .person-name { font-family: "Roboto", sans-serif; font-weight: 400; font-size: 17px; color: var(--brand-blue); line-height: 22px; }
  .contact .person-role { font-family: "Roboto Condensed", sans-serif; font-size: 14.5px; color: var(--ink); line-height: 18px; }
  .contact-list { margin-top: 18px; font-family: "Roboto Condensed", sans-serif; font-size: 12.5px; line-height: 16px; }
  .contact-row { display: flex; }
  .contact-row dt { width: 47px; color: var(--brand-blue); }
  .contact-row dd { color: var(--ink); }
  .company-line { position: absolute; left: 135px; top: 253px; font-family: "Roboto Condensed", sans-serif; font-size: 9px; color: var(--ink); }

  .back-lockup { left: 50%; top: 50%; transform: translate(-50%, -50%); font-size: 42px; color: var(--paper); gap: 12px; }
  .back-lockup .mark-circle { width: 72px; height: 64px; }
  .back-lockup .mark-square { width: 62px; height: 62px; }
  .alt-lockup { left: 50%; top: 50%; transform: translate(-50%, -50%); font-size: 40px; color: var(--brand-blue); }

  .caption { position: absolute; top: 940px; font-family: "Roboto", sans-serif; font-weight: 700; font-size: 21px; color: var(--label-navy); }
</style>
</head>
<body>
<main class="sheet">
  <!-- VoxHarbor front -->
  <section class="card card--front" style="left:126px; top:32px;">
    <div class="brand-lockup front-lockup"><span class="mark-circle"></span><span>voxharbor</span></div>
    <div class="contact">
      <p class="person-name">Ted Ramsell</p>
      <p class="person-role">Sales Director</p>
      <dl class="contact-list">
        <div class="contact-row"><dt>Mobile:</dt><dd>+61 428 163 907</dd></div>
        <div class="contact-row"><dt>Direct:</dt><dd>+61 3 9172 5836</dd></div>
        <div class="contact-row"><dt>Email:</dt><dd>ted@voxharbor.com.au</dd></div>
      </dl>
    </div>
    <p class="company-line">VoxHarbor (a brand of Quorvane Systems Pty Ltd)</p>
  </section>

  <!-- MyNimbusLinko front -->
  <section class="card card--front" style="left:597px; top:32px;">
    <div class="brand-lockup front-lockup"><span class="mark-square"></span><span>mynimbuslinko</span></div>
    <div class="contact" style="left:154px;">
      <p class="person-name">Ted Ramsell</p>
      <p class="person-role">Sales Director</p>
      <dl class="contact-list">
        <div class="contact-row"><dt>Mobile:</dt><dd>+61 428 163 907</dd></div>
        <div class="contact-row"><dt>Direct:</dt><dd>+61 3 9172 5836</dd></div>
        <div class="contact-row"><dt>Email:</dt><dd>ted@mynimbuslinko.com.au</dd></div>
      </dl>
    </div>
    <p class="company-line" style="left:154px;">MyNimbusLinko (a brand of Quorvane Systems Pty Ltd)</p>
  </section>

  <!-- Backs -->
  <section class="card card--back" style="left:127px; top:336px;">
    <div class="brand-lockup back-lockup"><span class="mark-circle"></span><span>voxharbor</span></div>
  </section>
  <section class="card card--back" style="left:594px; top:337px;">
    <div class="brand-lockup back-lockup"><span class="mark-square"></span><span>mynimbuslinko</span></div>
  </section>

  <!-- Alternative backs -->
  <section class="card card--back" style="left:128px; top:640px; width:453px; height:293px;">
    <div class="brand-lockup alt-lockup"><span>voxharbor</span></div>
  </section>
  <section class="card card--back" style="left:594px; top:640px; width:454px; height:293px;">
    <div class="brand-lockup alt-lockup"><span>mynimbuslinko</span></div>
  </section>

  <p class="caption" style="left:131px;">Alternative back</p>
  <p class="caption" style="left:594px;">Alternative back</p>
</main>
</body>
</html>
```